PowerPoint Template Design Project

Development of a custom PowerPoint template that is visually attractive.

Target Market(s)

Healthcare Executives

Requirements
Must have
• The template should complement our existing logo, although if the logo is seen as a problem, alternative designs will be considered. The template should provide a title page, table of contents page, header page, and end/back cover page. A recommended color palette should also be defined.

We would prefer that the body of the pages be white, with a watermark graphic (maybe a geometric pattern) that is very faded and fades to white. The watermark should not consume the slide and be limited to only a small amount of the slides printable areas.

The header background should also be a graphically rich element that works well with our existing logo.

The footer should be somewhat pronounced and give some weight to the slide without being overwhelming.

Using our logo's color and/or incorporating additional colors will be important to establishing a cohesive and professional look.
Should not have
• Colored gradients for backgrounds.
Serif Fonts
Text boxes with gradients

```html
<!DOCTYPE html>
<html lang="en">
<head>
<meta charset="utf-8">
<title>Title Slide</title>
<link rel="stylesheet" href="https://fonts.googleapis.com/css2?family=Questrial&family=Open+Sans:wght@400;700&display=swap">
<style>
  :root {
    --accent: #f04a1a;
    --ink: #3a3a3a;
    --text-grey: #5a5a5a;
    --brand-grey: #6d6e71;
    --rule: #e4e4e4;
    --footer-top: #f2f2f2;
    --footer-bottom: #d9d9d9;
    --paper: #ffffff;
  }
  * { margin: 0; padding: 0; box-sizing: border-box; }
  html, body { width: 1200px; height: 900px; overflow: hidden; background: var(--paper); }
  .slide {
    position: relative;
    width: 1200px;
    height: 900px;
    background: var(--paper);
    font-family: "Open Sans", sans-serif;
    overflow: hidden;
  }
  .watermark {
    position: absolute;
    left: 480px;
    top: 0;
    width: 720px;
    height: 780px;
    background: radial-gradient(ellipse at 80% 45%, rgba(200,200,200,0.45) 0%, rgba(225,225,225,0.25) 40%, rgba(255,255,255,0) 72%);
  }
  .brand {
    position: absolute;
    left: 892px;
    top: 285px;
    display: flex;
    align-items: center;
    gap: 14px;
  }
  .brand-mark {
    width: 92px;
    height: 92px;
    border-radius: 50%;
    background: var(--accent);
  }
  .brand-name {
    font-family: "Questrial", sans-serif;
    color: var(--brand-grey);
    font-size: 31px;
    line-height: 34px;
    letter-spacing: -0.5px;
  }
  .divider {
    position: absolute;
    left: 555px;
    right: 0;
    top: 387px;
    height: 2px;
    background: linear-gradient(to right, rgba(228,228,228,0), var(--rule) 30%);
  }
  .title-block {
    position: absolute;
    right: 40px;
    top: 412px;
    text-align: right;
  }
  .project-title {
    font-family: "Questrial", sans-serif;
    font-weight: 400;
    font-size: 49px;
    color: var(--ink);
    line-height: 1.1;
  }
  .project-title .highlight { color: var(--accent); }
  .project-date {
    margin-top: 14px;
    margin-right: 12px;
    font-weight: 700;
    font-size: 22px;
    color: var(--text-grey);
  }
  .project-summary {
    margin-top: 18px;
    margin-right: 12px;
    font-size: 20px;
    line-height: 33px;
    color: var(--text-grey);
  }
  .footer {
    position: absolute;
    left: 0;
    bottom: 0;
    width: 1200px;
    height: 70px;
    border-top: 4px solid var(--accent);
    background: linear-gradient(to bottom, var(--footer-top), var(--footer-bottom));
    display: flex;
    justify-content: space-between;
    align-items: center;
    padding: 0 40px 0 42px;
    font-weight: 700;
    font-size: 19px;
    color: var(--ink);
  }
</style>
</head>
<body>
  <main class="slide">
    <div class="watermark" role="img" aria-label="Faded grey dot-pattern watermark fading to white"></div>

    <div class="brand">
      <div class="brand-mark"></div>
      <div class="brand-name">CADENZA<br>PARTNERS</div>
    </div>

    <div class="divider"></div>

    <section class="title-block">
      <h1 class="project-title"><span class="highlight">Project</span> Title Here</h1>
      <p class="project-date">Date : 01 - 01 - 2013</p>
      <p class="project-summary">Sub text here Sub text here Sub text here Sub text here<br>Sub text here Sub text here Sub text here Sub</p>
    </section>

    <footer class="footer">
      <span class="page-number">Page No. 00</span>
      <span class="copyright">Copyright@2013</span>
    </footer>
  </main>
</body>
</html>
```